Menu and Logo Design for Dine in Indian restaurant

We are an Indian Restaurant(TaalVan) based in Ottawa, Ontario, Canada. We would like a menu designed for our dine-in customers. The interior of the restaurant is contemporary, fine-dine, prices are slightly on the premium side. We offer quality food and generous portions. The menu design should be clear and not too busy. Some menu items shall have descriptions .

Font styles to use
Decorative
Other font styles liked:
• Devnagari font and decorative font with mandala

Colors
59FF00
82FF00
B8FF75
E3FFCB
F4FFEA
E54698
E96AAD
F1A4CE
F9D9EA
FCEFF6

```html
<!DOCTYPE html>
<html lang="en">
<head>
<meta charset="utf-8">
<title>TaalVan – Dine-in Menu</title>
<link href="https://fonts.googleapis.com/css2?family=Cinzel:wght@600;700;900&family=Lato:wght@400;700&display=swap" rel="stylesheet">
<style>
:root{
  --page:#ffffff;
  --sheet:#0c0c0c;
  --ink:#f3f3f3;
  --muted:#a9a9a9;
  --gold:#f4b223;
  --accent:#e8461e;
  --pink:#e54698;
  --pink-soft:#f1a4ce;
  --green:#82ff00;
  --rule:#2a2a2a;
}
*{box-sizing:border-box;margin:0;padding:0}
html,body{width:1200px;height:2200px;overflow:hidden;background:var(--page)}
body{position:relative;font-family:'Lato',Arial,sans-serif;color:var(--ink)}
.sheet{position:absolute;left:100px;width:1000px;height:640px;background:var(--sheet);overflow:hidden;box-shadow:0 2px 6px rgba(0,0,0,.25)}
.sheet--outside{top:50px}
.sheet--inside{top:770px}
.sheet--back{top:1490px}
.border-band{position:absolute;left:0;right:0;height:12px;background:linear-gradient(90deg,var(--pink),var(--accent),var(--gold),var(--green),var(--pink))}
.border-band--top{top:0}
.border-band--bottom{bottom:0}
.col{position:absolute;top:30px;bottom:28px;width:300px}
.col--1{left:22px}.col--2{left:350px}.col--3{left:678px}
.fold{position:absolute;top:24px;bottom:24px;width:1px;background:var(--rule)}
.fold--a{left:333px}.fold--b{left:666px}
.section{margin-bottom:12px}
.section h3{font-family:'Cinzel',Georgia,serif;font-weight:700;font-size:13px;letter-spacing:1.5px;color:var(--gold);text-align:center;margin-bottom:3px}
.section h3::after{content:"";display:block;width:40px;height:2px;background:var(--accent);margin:3px auto 0}
.item{display:flex;justify-content:space-between;font-size:9.5px;line-height:14px;text-transform:uppercase;letter-spacing:.3px}
.item .price{color:var(--gold);font-weight:700}
.desc{font-size:8.5px;line-height:11px;color:var(--muted);margin-bottom:3px}
.photo{border-radius:50%;background:radial-gradient(circle at 40% 40%,#f0c36b,#c0601f 60%,#4a2208)}
.photo--green{background:radial-gradient(circle at 40% 40%,#f4f0d8,#b8b27a 55%,#4d4a25)}
.photo--rice{background:radial-gradient(circle at 40% 40%,#fff1b0,#e3a92c 60%,#6b4310)}
.photo--dosa{border-radius:8px;background:linear-gradient(135deg,#f6d491,#c98a36 60%,#5c3810)}
.photo-row{display:flex;justify-content:space-around;margin:6px 0}
.split{display:flex;gap:10px;align-items:flex-start}
.split .list{flex:1}
.cover{text-align:center}
.brand{font-family:'Cinzel',Georgia,serif;font-weight:900;font-size:46px;color:var(--accent);letter-spacing:2px;margin-top:6px}
.brand-sub{font-family:'Cinzel',Georgia,serif;font-size:12px;color:var(--gold);letter-spacing:4px;margin-top:2px}
.plate{width:250px;height:250px;margin:18px auto 18px;border-radius:50%;background:radial-gradient(circle,#3b2a20 0,#1c1512 55%,#2d2d2d 70%,#111 100%)}
.contact{font-size:10.5px;line-height:18px;color:var(--ink);display:flex;align-items:center;justify-content:center;gap:6px}
.contact svg{width:12px;height:12px;fill:var(--gold)}
.web{font-family:'Cinzel',Georgia,serif;font-size:12px;color:var(--gold);text-align:center;letter-spacing:1px;margin-top:6px}
</style>
</head>
<body>

<!-- Outside spread -->
<section class="sheet sheet--outside">
  <div class="border-band border-band--top"></div>
  <div class="fold fold--a"></div><div class="fold fold--b"></div>

  <div class="col col--1">
    <div class="section split">
      <div class="list">
        <h3>Street Menu</h3>
        <div class="item"><span>Bombay Vada Pav</span><span class="price">8</span></div>
        <div class="item"><span>Pani Puri Shots</span><span class="price">9</span></div>
        <div class="item"><span>Samosa Chaat</span><span class="price">10</span></div>
        <div class="item"><span>Papdi Chaat</span><span class="price">10</span></div>
        <div class="item"><span>Dahi Bhalla</span><span class="price">11</span></div>
      </div>
      <div class="photo" style="width:70px;height:70px" role="img" aria-label="Photo of chaat platter"></div>
    </div>
    <div class="section split">
      <div class="photo" style="width:70px;height:70px" role="img" aria-label="Photo of biryani bowl"></div>
      <div class="list">
        <h3>Biryani</h3>
        <div class="item"><span>Veg Dum Biryani</span><span class="price">18</span></div>
        <div class="item"><span>Chicken Biryani</span><span class="price">21</span></div>
        <div class="item"><span>Lamb Biryani</span><span class="price">24</span></div>
        <div class="item"><span>Prawn Biryani</span><span class="price">25</span></div>
      </div>
    </div>
    <div class="section">
      <h3>Sides</h3>
      <div class="item"><span>Cucumber Raita</span><span class="price">5</span></div>
      <div class="item"><span>Papadum Basket</span><span class="price">4</span></div>
      <div class="item"><span>Mango Chutney</span><span class="price">3</span></div>
      <div class="item"><span>Mixed Pickle</span><span class="price">3</span></div>
      <div class="item"><span>Onion Salad</span><span class="price">4</span></div>
    </div>
    <div class="photo-row">
      <div class="photo" style="width:46px;height:46px" role="img" aria-label="Photo of raita"></div>
      <div class="photo photo--rice" style="width:46px;height:46px" role="img" aria-label="Photo of chutney"></div>
      <div class="photo" style="width:46px;height:46px" role="img" aria-label="Photo of pickle"></div>
    </div>
    <div class="section">
      <h3>Breads</h3>
      <div class="item"><span>Butter Naan</span><span class="price">4</span></div>
      <div class="item"><span>Garlic Naan</span><span class="price">5</span></div>
      <div class="item"><span>Tandoori Roti</span><span class="price">4</span></div>
    </div>
  </div>

  <div class="col col--2">
    <div class="photo-row">
      <div class="photo photo--rice" style="width:110px;height:110px" role="img" aria-label="Photo of rice and dal platter"></div>
    </div>
    <div class="section">
      <h3>Rice &amp; Dal</h3>
      <div class="item"><span>Plain Basmati</span><span class="price">5</span></div>
      <div class="item"><span>Jeera Rice</span><span class="price">6</span></div>
      <div class="item"><span>Lemon Rice</span><span class="price">7</span></div>
      <div class="item"><span>Dal Tadka</span><span class="price">14</span></div>
      <div class="item"><span>Dal Makhani</span><span class="price">15</span></div>
      <div class="item"><span>Chana Masala</span><span class="price">15</span></div>
    </div>
    <div class="section split">
      <div class="list">
        <h3>Beverages</h3>
        <div class="item"><span>Masala Chai</span><span class="price">4</span></div>
        <div class="item"><span>Mango Lassi</span><span class="price">6</span></div>
        <div class="item"><span>Rose Lassi</span><span class="price">6</span></div>
        <div class="item"><span>Nimbu Soda</span><span class="price">5</span></div>
      </div>
      <div class="photo photo--green" style="width:64px;height:64px" role="img" aria-label="Photo of lassi glass"></div>
    </div>
    <div class="section">
      <h3>Desserts</h3>
      <div class="item"><span>Gulab Jamun</span><span class="price">7</span></div>
      <div class="item"><span>Ras Malai</span><span class="price">8</span></div>
      <div class="item"><span>Kulfi Falooda</span><span class="price">9</span></div>
      <div class="item"><span>Gajar Halwa</span><span class="price">8</span></div>
    </div>
    <div class="photo-row">
      <div class="photo" style="width:60px;height:60px" role="img" aria-label="Photo of gulab jamun"></div>
    </div>
  </div>

  <div class="col col--3 cover">
    <div class="brand">TaalVan</div>
    <div class="brand-sub">Indian Kitchen</div>
    <div class="plate" role="img" aria-label="Photo of a dark plate holding wooden spoons of colourful Indian spices"></div>
    <div class="contact"><svg viewBox="0 0 24 24"><path d="M6.6 10.8a15 15 0 0 0 6.6 6.6l2.2-2.2a1 1 0 0 1 1-.25 11.4 11.4 0 0 0 3.6.6 1 1 0 0 1 1 1V20a1 1 0 0 1-1 1A17 17 0 0 1 3 4a1 1 0 0 1 1-1h3.5a1 1 0 0 1 1 1c0 1.25.2 2.45.6 3.6a1 1 0 0 1-.25 1z"/></svg>613-555-0179 &nbsp;|&nbsp; hello@taalvan.ca</div>
    <div class="contact"><svg viewBox="0 0 24 24"><path d="M12 2a7 7 0 0 0-7 7c0 5.2 7 13 7 13s7-7.8 7-13a7 7 0 0 0-7-7zm0 9.5A2.5 2.5 0 1 1 12 6.5a2.5 2.5 0 0 1 0 5z"/></svg>Unit 5, 120 Maple Rd, Ottawa, ON K2P 0X1</div>
  </div>
  <div class="border-band border-band--bottom"></div>
</section>

<!-- Inside spread -->
<section class="sheet sheet--inside">
  <div class="border-band border-band--top"></div>
  <div class="fold fold--a"></div><div class="fold fold--b"></div>

  <div class="col col--1">
    <div class="section split">
      <div class="list">
        <h3>Soups</h3>
        <div class="item"><span>Tomato Shorba</span><span class="price">7</span></div>
        <div class="item"><span>Mulligatawny</span><span class="price">8</span></div>
        <div class="item"><span>Sweet Corn Soup</span><span class="price">7</span></div>
      </div>
      <div class="photo" style="width:64px;height:64px" role="img" aria-label="Photo of soup bowl"></div>
    </div>
    <div class="photo-row">
      <div class="photo photo--dosa" style="width:200px;height:60px" role="img" aria-label="Photo of sandwich appetizer"></div>
    </div>
    <div class="section">
      <h3>Appetizers</h3>
      <div class="item"><span>Veg Samosa (2)</span><span class="price">7</span></div>
      <div class="item"><span>Onion Bhaji</span><span class="price">8</span></div>
      <div class="item"><span>Paneer Pakora</span><span class="price">11</span></div>
      <div class="item"><span>Hara Bhara Kebab</span><span class="price">12</span></div>
      <div class="item"><span>Chilli Paneer</span><span class="price">14</span></div>
      <div class="item"><span>Gobi Manchurian</span><span class="price">13</span></div>
      <div class="item"><span>Chicken 65</span><span class="price">15</span></div>
      <div class="item"><span>Chilli Chicken</span><span class="price">15</span></div>
      <div class="item"><span>Chicken Lollipop</span><span class="price">15</span></div>
      <div class="item"><span>Fish Amritsari</span><span class="price">16</span></div>
      <div class="item"><span>Tandoori Wings</span><span class="price">14</span></div>
      <div class="item"><span>Lamb Seekh Kebab</span><span class="price">17</span></div>
      <div class="item"><span>Prawn Koliwada</span><span class="price">18</span></div>
      <div class="item"><span>Mixed Veg Platter</span><span class="price">19</span></div>
      <div class="item"><span>Non-Veg Platter</span><span class="price">24</span></div>
    </div>
  </div>

  <div class="col col--2">
    <div class="section split">
      <div class="list">
        <h3>Tandoor</h3>
        <div class="item"><span>Paneer Tikka</span><span class="price">16</span></div>
        <div class="item"><span>Malai Broccoli</span><span class="price">15</span></div>
        <div class="item"><span>Chicken Tikka</span><span class="price">17</span></div>
        <div class="item"><span>Tandoori Chicken</span><span class="price">19</span></div>
        <div class="item"><span>Lamb Chops</span><span class="price">26</span></div>
      </div>
      <div class="photo" style="width:64px;height:64px" role="img" aria-label="Photo of tandoori dish"></div>
    </div>
    <div class="section">
      <h3>Chaat Corner</h3>
      <div class="desc">Crisp puris, tangy tamarind, mint chutney and sweet yoghurt.</div>
      <div class="item"><span>Bhel Puri</span><span class="price">9</span></div>
      <div class="item"><span>Aloo Tikki Chaat</span><span class="price">10</span></div>
      <div class="item"><span>Raj Kachori</span><span class="price">11</span></div>
    </div>
    <div class="photo-row">
      <div class="photo photo--rice" style="width:70px;height:70px" role="img" aria-label="Photo of chaat"></div>
    </div>
    <div class="section">
      <h3>Kids Menu</h3>
      <div class="desc">Mild flavours, smaller plates, served with fries.</div>
      <div class="item"><span>Butter Chicken Bowl</span><span class="price">11</span></div>
      <div class="item"><span>Cheese Naan</span><span class="price">7</span></div>
      <div class="item"><span>Mini Dosa</span><span class="price">8</span></div>
    </div>
    <div class="photo-row">
      <div class="photo photo--dosa" style="width:150px;height:50px" role="img" aria-label="Photo of rolled dosa"></div>
    </div>
    <div class="photo-row">
      <div class="photo photo--green" style="width:60px;height:60px" role="img" aria-label="Photo of idli"></div>
    </div>
  </div>

  <div class="col col--3">
    <div class="photo-row">
      <div class="photo photo--dosa" style="width:220px;height:110px" role="img" aria-label="Photo of masala dosa with chutneys"></div>
    </div>
    <div class="section">
      <h3>South Indian</h3>
      <div class="item"><span>Plain Dosa</span><span class="price">11</span></div>
      <div class="item"><span>Masala Dosa</span><span class="price">13</span></div>
      <div class="item"><span>Mysore Masala Dosa</span><span class="price">14</span></div>
      <div class="item"><span>Paneer Dosa</span><span class="price">15</span></div>
      <div class="item"><span>Onion Rava Dosa</span><span class="price">14</span></div>
      <div class="item"><span>Ghee Roast Dosa</span><span class="price">14</span></div>
      <div class="item"><span>Spring Dosa</span><span class="price">15</span></div>
      <div class="item"><span>Chicken Dosa</span><span class="price">16</span></div>
      <div class="item"><span>Idli Sambar</span><span class="price">10</span></div>
      <div class="item"><span>Medu Vada</span><span class="price">10</span></div>
      <div class="item"><span>Onion Uttapam</span><span class="price">13</span></div>
      <div class="item"><span>Tomato Uttapam</span><span class="price">13</span></div>
      <div class="item"><span>Mixed Veg Uttapam</span><span class="price">14</span></div>
      <div class="item"><span>Pongal</span><span class="price">12</span></div>
    </div>
    <div class="web">www.taalvan.ca</div>
  </div>
  <div class="border-band border-band--bottom"></div>
</section>

<!-- Back spread -->
<section class="sheet sheet--back">
  <div class="border-band border-band--top"></div>
  <div class="fold fold--a"></div><div class="fold fold--b"></div>

  <div class="col col--1">
    <div class="photo-row">
      <div class="photo" style="width:80px;height:80px" role="img" aria-label="Photo of thali plate"></div>
      <div class="photo photo--rice" style="width:80px;height:80px" role="img" aria-label="Photo of curry bowl"></div>
    </div>
    <div class="section">
      <h3>Thali</h3>
      <div class="desc">A complete meal with two curries, dal, rice, naan, raita and dessert.</div>
      <div class="item"><span>Veg Thali</span><span class="price">22</span></div>
      <div class="item"><span>Chicken Thali</span><span class="price">25</span></div>
      <div class="item"><span>Lamb Thali</span><span class="price">27</span></div>
      <div class="item"><span>Royal Thali</span><span class="price">32</span></div>
    </div>
    <div class="photo-row">
      <div class="photo photo--green" style="width:110px;height:80px" role="img" aria-label="Photo of noodles dish"></div>
    </div>
    <div class="section">
      <h3>Indo-Chinese</h3>
      <div class="item"><span>Veg Hakka Noodles</span><span class="price">14</span></div>
      <div class="item"><span>Chicken Noodles</span><span class="price">16</span></div>
      <div class="item"><span>Veg Fried Rice</span><span class="price">13</span></div>
      <div class="item"><span>Egg Fried Rice</span><span class="price">14</span></div>
      <div class="item"><span>Schezwan Rice</span><span class="price">15</span></div>
      <div class="item"><span>Chilli Garlic Noodles</span><span class="price">15</span></div>
      <div class="item"><span>Veg Manchurian</span><span class="price">14</span></div>
      <div class="item"><span>Prawn Fried Rice</span><span class="price">18</span></div>
    </div>
  </div>

  <div class="col col--2">
    <div class="section">
      <h3>Veg Curries</h3>
      <div class="item"><span>Paneer Butter Masala</span><span class="price">17</span></div>
      <div class="desc">Cottage cheese in a rich tomato and cashew gravy.</div>
      <div class="item"><span>Palak Paneer</span><span class="price">17</span></div>
      <div class="desc">Fresh spinach purée with cubes of paneer.</div>
      <div class="item"><span>Malai Kofta</span><span class="price">17</span></div>
      <div class="desc">Soft dumplings in a creamy saffron sauce.</div>
      <div class="item"><span>Kadai Paneer</span><span class="price">17</span></div>
      <div class="desc">Peppers, onions and paneer with kadai spices.</div>
      <div class="item"><span>Aloo Gobi</span><span class="price">15</span></div>
      <div class="desc">Potato and cauliflower tossed with cumin.</div>
      <div class="item"><span>Bhindi Masala</span><span class="price">15</span></div>
      <div class="desc">Okra stir-fried with onion and tomato.</div>
      <div class="item"><span>Baingan Bharta</span><span class="price">15</span></div>
      <div class="desc">Smoked eggplant mash with green peas.</div>
      <div class="item"><span>Navratan Korma</span><span class="price">16</span></div>
      <div class="desc">Nine vegetables in a mild nutty cream.</div>
      <div class="item"><span>Mushroom Matar</span><span class="price">15</span></div>
      <div class="desc">Mushrooms and peas in a spiced onion gravy.</div>
    </div>
    <div class="web">www.taalvan.ca</div>
  </div>

  <div class="col col--3">
    <div class="section">
      <h3>Non-Veg Curries</h3>
      <div class="item"><span>Butter Chicken</span><span class="price">19</span></div>
      <div class="desc">Tandoori chicken in a velvety tomato butter sauce.</div>
      <div class="item"><span>Chicken Tikka Masala</span><span class="price">19</span></div>
      <div class="desc">Charred tikka in a spiced onion tomato masala.</div>
      <div class="item"><span>Chicken Korma</span><span class="price">19</span></div>
      <div class="desc">Mild curry with cream, almonds and cardamom.</div>
      <div class="item"><span>Chicken Vindaloo</span><span class="price">19</span></div>
      <div class="desc">Fiery Goan curry with vinegar and chillies.</div>
      <div class="item"><span>Lamb Rogan Josh</span><span class="price">23</span></div>
      <div class="desc">Kashmiri lamb slow cooked with aromatic spices.</div>
      <div class="item"><span>Lamb Saag</span><span class="price">23</span></div>
      <div class="desc">Tender lamb simmered with spinach and garlic.</div>
      <div class="item"><span>Goat Curry</span><span class="price">24</span></div>
      <div class="desc">Bone-in goat in a home-style onion gravy.</div>
      <div class="item"><span>Goan Fish Curry</span><span class="price">22</span></div>
      <div class="desc">Fish fillets in coconut, tamarind and chilli.</div>
      <div class="item"><span>Prawn Malai Curry</span><span class="price">24</span></div>
      <div class="desc">Tiger prawns in a light coconut cream sauce.</div>
      <div class="item"><span>Egg Curry</span><span class="price">15</span></div>
      <div class="desc">Boiled eggs in a tangy tomato onion masala.</div>
    </div>
  </div>
  <div class="border-band border-band--bottom"></div>
</section>

</body>
</html>
```